Pineapple Cane Spirit Label

We are needing a pineapple infused label for our up coming release.

This can be as out there as you like but must have the company logo at the forefront. The label must also compliment the other 3 skus we have. The final design should show a classy and refined label that works for both the home bar, bottle shop and restaurant.

```html
<!DOCTYPE html>
<html lang="en">
<head>
<meta charset="utf-8">
<title>Marlow Bay Rum Co — Pineapple Label</title>
<link rel="stylesheet" href="https://fonts.googleapis.com/css2?family=Alfa+Slab+One&family=Cormorant+Garamond:wght@600&display=swap">
<style>
  :root {
    --backdrop: #6b6864;
    --label-ink: #1d1c1f;
    --cream: #e4d3ac;
    --cream-soft: #c9b78f;
    --ornament-tone: #8d7f63;
  }
  * { margin: 0; padding: 0; box-sizing: border-box; }
  html, body { width: 769px; height: 1200px; overflow: hidden; }
  body {
    background: var(--backdrop);
    position: relative;
    font-family: "Cormorant Garamond", serif;
  }
  .label {
    position: absolute;
    left: 104px;
    top: 150px;
    width: 560px;
    height: 900px;
  }
  .label__shape { position: absolute; inset: 0; }
  .label__art {
    position: absolute;
    border-radius: 6px;
    background: radial-gradient(ellipse at center, var(--ornament-tone) 0%, #4a4335 70%, var(--label-ink) 100%);
    opacity: .85;
  }
  .label__art--ship { left: 165px; top: 60px; width: 230px; height: 275px; }
  .label__art--pineapple-left { left: 66px; top: 185px; width: 80px; height: 150px; }
  .label__art--pineapple-right { left: 414px; top: 185px; width: 80px; height: 150px; }
  .label__art--flourish { left: 130px; top: 718px; width: 300px; height: 68px; }
  .brand-name {
    position: absolute; left: 0; right: 0; top: 372px;
    text-align: center;
    font-family: "Cormorant Garamond", serif;
    font-weight: 600;
    color: var(--cream);
    font-size: 58px;
    letter-spacing: 4px;
    line-height: 1.1;
    text-transform: uppercase;
  }
  .brand-name__sub { display: block; font-size: 28px; letter-spacing: 10px; }
  .flavour {
    position: absolute; left: 0; right: 0; top: 535px;
    font-family: "Alfa Slab One", serif;
    color: var(--cream);
    text-align: center;
    text-transform: uppercase;
    font-size: 58px; letter-spacing: 3px; line-height: 1;
  }
  .provenance {
    position: absolute; left: 0; right: 0; top: 612px;
    text-align: center; color: var(--cream-soft);
    font-size: 16px; letter-spacing: 3px; line-height: 1.3;
    text-transform: uppercase;
  }
  .provenance__year { font-size: 19px; color: var(--cream); }
  .provenance__star { font-size: 18px; color: var(--cream); }
  .volume {
    position: absolute; left: 0; right: 0; top: 800px;
    text-align: center; color: var(--cream);
    font-size: 18px; letter-spacing: 3px;
  }
</style>
</head>
<body>
  <section class="label">
    <svg class="label__shape" viewBox="0 0 560 900" width="560" height="900" aria-hidden="true">
      <path d="M40 120 L140 120 L180 40 L280 0 L380 40 L420 120 L520 120 L520 560 L560 600 L520 640 L520 800 L280 900 L40 800 L40 640 L0 600 L40 560 Z" fill="var(--label-ink)"/>
      <path d="M52 132 L148 132 L188 52 L280 14 L372 52 L412 132 L508 132 L508 565 L544 600 L508 635 L508 792 L280 886 L52 792 L52 635 L16 600 L52 565 Z" fill="none" stroke="var(--cream)" stroke-width="2.5"/>
      <path d="M62 142 L154 142 L194 62 L280 26 L366 62 L406 142 L498 142 L498 570 L530 600 L498 630 L498 785 L280 874 L62 785 L62 630 L30 600 L62 570 Z" fill="none" stroke="var(--cream-soft)" stroke-width="1"/>
    </svg>

    <div class="label__art label__art--ship" role="img" aria-label="Engraved tall ship under full sail on waves with starry sky"></div>
    <div class="label__art label__art--pineapple-left" role="img" aria-label="Engraved pineapple ornament"></div>
    <div class="label__art label__art--pineapple-right" role="img" aria-label="Engraved pineapple ornament"></div>

    <h1 class="brand-name">Marlow Bay<span class="brand-name__sub">Rum Co</span></h1>

    <h2 class="flavour">Pineapple</h2>
    <p class="provenance">
      Established at Sea<br>
      <span class="provenance__year">1806</span><br>
      Australia<br>
      <span class="provenance__star">✶</span>
    </p>

    <div class="label__art label__art--flourish" role="img" aria-label="Engraved leafy flourish ornament"></div>
    <p class="volume">• 700 ML • 45 ALC/VOL •</p>
  </section>
</body>
</html>
```